PELDRAX Business Cards

We require a business card for our company that provides IT consulting services. We already have a logo that needs to be used on the card. We want a clean professional looking design that incorporates our colours. Our main focus is providing managed services to business, which involves us looking after all of their IT requirements including managing servers/networks, projects, and procurement.

Industry/Entity Type

Information Technology

Requirements
Must have
• our logo, contact information, name, title, phone numbers

```html
<!DOCTYPE html>
<html lang="en">
<head>
<meta charset="utf-8">
<title>PELDRAX Business Card</title>
<link rel="stylesheet" href="https://fonts.googleapis.com/css2?family=Roboto+Slab:wght@700&family=Questrial&display=swap">
<style>
  :root {
    --backdrop: #fb6a5c;
    --card: #ffffff;
    --ink-dark: #2b2b2b;
    --ink-body: #3a3a3a;
    --ink-muted: #6a6a6a;
    --accent-blue: #1e8fcb;
  }
  html, body {
    margin: 0;
    padding: 0;
    width: 1200px;
    height: 790px;
    overflow: hidden;
    background: var(--backdrop);
  }
  .business-card {
    position: absolute;
    left: 150px;
    top: 133px;
    width: 900px;
    height: 523px;
    background: var(--card);
    box-shadow: 0 6px 24px rgba(0, 0, 0, 0.12);
  }
  .brand {
    position: absolute;
    top: 36px;
    left: 0;
    width: 100%;
    display: flex;
    justify-content: center;
    align-items: center;
    gap: 10px;
  }
  .brand-mark {
    width: 14px;
    height: 14px;
    background: var(--accent-blue);
  }
  .brand-name {
    font-family: "Questrial", sans-serif;
    font-size: 20px;
    line-height: 1;
    letter-spacing: 4px;
    color: var(--ink-body);
  }
  .holder-name {
    position: absolute;
    top: 92px;
    left: 0;
    width: 100%;
    margin: 0;
    text-align: center;
    font-family: "Roboto Slab", serif;
    font-weight: 700;
    font-size: 34px;
    letter-spacing: 2px;
    line-height: 1;
    color: var(--ink-dark);
  }
  .holder-title {
    position: absolute;
    top: 140px;
    left: 0;
    width: 100%;
    margin: 0;
    text-align: center;
    font-family: "Questrial", sans-serif;
    font-size: 18px;
    letter-spacing: 3px;
    line-height: 1;
    color: var(--ink-muted);
  }
  .name-rule {
    position: absolute;
    top: 180px;
    left: 210px;
    width: 480px;
    height: 6px;
    background: var(--accent-blue);
  }
  .contact-line {
    position: absolute;
    left: 0;
    width: 100%;
    margin: 0;
    text-align: center;
    font-family: "Questrial", sans-serif;
    font-size: 26px;
    line-height: 1;
    letter-spacing: 2px;
    color: var(--ink-body);
  }
  .contact-phone { top: 262px; font-size: 28px; }
  .contact-email { top: 340px; }
  .contact-web   { top: 418px; }
</style>
</head>
<body>
  <main class="business-card">
    <div class="brand">
      <span class="brand-mark"></span>
      <span class="brand-name">PELDRAX</span>
    </div>
    <h1 class="holder-name">NAME HERE</h1>
    <p class="holder-title">IT CONSULTANT</p>
    <div class="name-rule"></div>
    <p class="contact-line contact-phone">0048193726</p>
    <p class="contact-line contact-email">info&nbsp; peldrax.com</p>
    <p class="contact-line contact-web">www.peldrax.com</p>
  </main>
</body>
</html>
```